Business Card for a mobile physiotherapy company

I need a layout for a business card for a mobile physiotherapy company.
Slogan is "Mobile Physiotherapy - Your Road To Recovery"
Phone number is 867-402-5913
Email VantrePhysio@mailbright.ca (subject to change with website)
Website www.VantrePhysio.ca
My name and credentials: Kent Vantre Kent Vantre, BSc(kin), MPT, CAFCI, IMS
Information maybe included: Direct Billing, Services including Physiotherapy, IMS, acupuncture
Maybe include facebook and instagram logos
One side with the logo clean and sharp
Other side with details, try not to look too busy, keep everything concise

```html
<!DOCTYPE html>
<html lang="en">
<head>
<meta charset="utf-8">
<title>Vantre Therapy – Business Card</title>
<link rel="stylesheet" href="https://fonts.googleapis.com/css2?family=Lato:wght@400;700;900&display=swap">
<style>
  :root {
    --stage: #3b3b3b;
    --paper: #f3f3f1;
    --ink: #111418;
    --navy: #2c4a72;
    --navy-soft: #3c5c88;
    --bullet: #3a55a0;
    --accent: #b0387a;
  }
  * { box-sizing: border-box; margin: 0; padding: 0; }
  html, body {
    width: 1200px; height: 755px; overflow: hidden;
    background: var(--stage);
    font-family: "Lato", Arial, sans-serif;
  }
  .card {
    position: absolute;
    top: 218px;
    width: 500px; height: 287px;
    background: var(--paper);
    overflow: hidden;
  }
  .card--front { left: 88px; }
  .card--back { left: 617px; }

  .holder { position: absolute; left: 40px; top: 96px; }
  .holder__name { font-size: 26px; font-weight: 900; color: var(--ink); letter-spacing: -0.2px; line-height: 32px; }
  .holder__credentials { font-size: 12px; color: var(--ink); margin-top: 8px; line-height: 16px; }
  .holder__rule { width: 26px; height: 2px; background: var(--bullet); margin-top: 11px; }
  .social { display: flex; gap: 7px; margin-top: 30px; }
  .social__dot { width: 22px; height: 22px; border-radius: 50%; background: var(--bullet); }
  .social__dot--alt { background: var(--accent); }

  .services { position: absolute; left: 284px; top: 91px; list-style: none; }
  .services li {
    font-size: 12px; color: var(--ink); line-height: 15.5px;
    padding-left: 14px; position: relative;
  }
  .services li::before {
    content: ""; position: absolute; left: 0; top: 5px;
    width: 7px; height: 7px; border-radius: 50%; background: var(--bullet);
  }
  .contact {
    position: absolute; left: 284px; top: 166px;
    border-left: 2px solid var(--bullet);
    padding-left: 9px;
    font-style: normal;
    font-size: 12px; color: var(--ink); line-height: 16px;
  }
  .corner-art {
    position: absolute; right: 4px; bottom: 38px;
    width: 64px; height: 32px;
    background: linear-gradient(180deg, var(--navy-soft), var(--navy));
  }
  .slogan-band {
    position: absolute; left: 0; right: 0; bottom: 0; height: 38px;
    background: var(--navy);
    display: flex; align-items: center; justify-content: center;
    color: #fff; font-size: 15.5px; font-weight: 700; letter-spacing: 0.9px;
    text-transform: uppercase;
  }

  .brand {
    position: absolute; inset: 0;
    display: flex; flex-direction: column; align-items: center; justify-content: center;
    gap: 12px;
  }
  .brand__mark { width: 40px; height: 40px; border-radius: 50%; background: var(--navy); }
  .brand__name {
    font-size: 30px; font-weight: 700; color: var(--navy);
    letter-spacing: 3px; text-transform: uppercase; text-align: center; line-height: 1.1;
  }
</style>
</head>
<body>
  <section class="card card--front">
    <div class="holder">
      <h1 class="holder__name">Kent Vantre</h1>
      <p class="holder__credentials">BSc(kin), MPT, CAFCI, IMS</p>
      <div class="holder__rule"></div>
      <div class="social">
        <span class="social__dot" aria-label="Social profile"></span>
        <span class="social__dot social__dot--alt" aria-label="Social profile"></span>
      </div>
    </div>
    <ul class="services">
      <li>Direct Billing</li>
      <li>Services including Physiotherapy</li>
      <li>IMS</li>
      <li>acupuncture</li>
    </ul>
    <address class="contact">
      867-402-5913<br>
      www.VantrePhysio.ca<br>
      VantrePhysio@mailbright.ca
    </address>
    <div class="corner-art" role="img" aria-label="Brand mark decoration area"></div>
    <div class="slogan-band">Mobile Physiotherapy - Your Road to Recovery</div>
  </section>

  <section class="card card--back">
    <div class="brand">
      <span class="brand__mark"></span>
      <p class="brand__name">Vantre Therapy</p>
    </div>
  </section>
</body>
</html>
```